New Infusion Pharmacy needs Business Card design

Hello!

We are Verant Infusion Pharmacy, are we are looking for a two sided, clean and modern business card.

First, let me give you a little bit about what an infusion pharmacy does...
We compound and fill prescriptions for drugs that are injectable, meaning that they are administered via an IV bag or a syringe. Basically anything that is too advanced for a normal pill pharmacy to fill. We compound everything in our state of the art clean room, then deliver it directly to the patients home. We have an outside sales force that markets to hospitals, home health agencies, and doctor's offices.

as for the business card...
We are looking for a clean, modern card. our colors are in our logo, kind of a light bule and a darker blue. We do really like the rounded corners on the card. Also, we would like the back of the card to be the reverse colors of the front, for example, if the front of the card has a light background, then the back of the card will have a dark background.

On the back side of the card we want to have our logo, then list some of the services we offer:
-IVIG
-TPN
-Enteral Nutrition
-IV Antibiotics
-IV Hydration
-Blood Factors
-Chemotherapy
-Pain Management

Our logo is uploaded in .psd format, if you need a different format let me know and i'll throw it up here.

Thank you so much!!

Industry/Entity Type

Pharmacy

Requirements
Must have
• Front of Card: (no particular order, please arrange in whatever way you think looks best!)
-Employee Name
-Title
-Office Phone #
-Cell Phone #
-Fax #
-email address - marlo@verantcareinfuse.com
-office address - 4127 Delmore St. Alder Vale, CA 90418
-Web Site - www.verantcareinfuse.com

```html
<!DOCTYPE html>
<html lang="en">
<head>
<meta charset="utf-8">
<title>Verant Infusion Pharmacy – Business Card</title>
<link rel="stylesheet" href="https://fonts.googleapis.com/css2?family=Didact+Gothic&family=Arimo:wght@400;700&display=swap">
<style>
  :root {
    --stage: #eceeef;
    --card-white: #ffffff;
    --brand-dark: #0d5670;
    --brand-light: #139bc6;
    --title-blue: #2c9bd0;
    --ink: #1f2a30;
    --rule-grey: #c9cfd3;
    --white: #ffffff;
  }
  * { box-sizing: border-box; margin: 0; padding: 0; }
  html, body { width: 1200px; height: 702px; overflow: hidden; background: var(--stage); }
  .stage { position: relative; width: 1200px; height: 702px; display: flex; align-items: center; justify-content: center; gap: 44px; }
  .card { position: relative; width: 540px; height: 310px; border-radius: 22px; overflow: hidden; box-shadow: 0 6px 18px rgba(0,0,0,.18); }

  /* Front */
  .card-front { background: var(--card-white); font-family: "Arimo", Arial, sans-serif; color: var(--ink); }
  .company-name { position: absolute; font-family: "Arimo", Arial, sans-serif; font-weight: 700; white-space: nowrap; }
  .front-name { left: 34px; top: 106px; font-size: 17px; color: var(--brand-dark); }
  .divider { position: absolute; left: 272px; top: 40px; width: 1px; height: 150px; background: var(--rule-grey); }
  .contact { position: absolute; left: 290px; top: 44px; }
  .employee-name { font-size: 21px; font-weight: 700; color: var(--brand-dark); line-height: 1.1; }
  .employee-title { font-size: 13px; color: var(--title-blue); margin-bottom: 12px; }
  .contact-list { list-style: none; font-size: 13.5px; }
  .contact-list li { display: flex; align-items: center; gap: 6px; height: 22px; }
  .contact-list svg { width: 11px; height: 11px; fill: var(--ink); flex: none; }
  .band-rule { position: absolute; left: 0; width: 100%; height: 1px; background: var(--brand-light); }
  .band-rule.top { top: 214px; }
  .band-rule.bottom { top: 256px; }
  .web-band { position: absolute; left: 0; top: 219px; width: 100%; height: 33px; background: var(--brand-dark); color: var(--white); font-size: 14px; letter-spacing: 2px; display: flex; align-items: center; justify-content: center; }
  .address { position: absolute; left: 0; top: 268px; width: 100%; text-align: center; font-size: 14px; letter-spacing: 1.2px; }

  /* Back */
  .card-back { background: var(--brand-light); color: var(--white); font-family: "Didact Gothic", sans-serif; }
  .services-heading { position: absolute; left: 36px; top: 34px; font-family: "Arimo", Arial, sans-serif; font-weight: 700; font-size: 21px; }
  .services-list { position: absolute; left: 40px; top: 74px; list-style: none; font-size: 17px; line-height: 25px; letter-spacing: .8px; }
  .services-list li::before { content: "•"; margin-right: 8px; }
  .back-name { left: 282px; top: 140px; font-size: 19px; color: var(--white); }
  .back-web { position: absolute; left: 282px; top: 246px; font-size: 15px; letter-spacing: 1.6px; }
</style>
</head>
<body>
<main class="stage">
  <section class="card card-front" aria-label="Business card front">
    <p class="company-name front-name">Verant Infusion Pharmacy</p>
    <div class="divider"></div>
    <div class="contact">
      <p class="employee-name">Employee Name</p>
      <p class="employee-title">Title</p>
      <ul class="contact-list">
        <li><svg viewBox="0 0 24 24" aria-hidden="true"><path d="M6.6 10.8a15 15 0 0 0 6.6 6.6l2.2-2.2a1 1 0 0 1 1-.25 11.4 11.4 0 0 0 3.6.57 1 1 0 0 1 1 1V20a1 1 0 0 1-1 1A17 17 0 0 1 3 4a1 1 0 0 1 1-1h3.5a1 1 0 0 1 1 1c0 1.250.2 2.45.57 3.57a1 1 0 0 1-.25 1z"/></svg>0987 654321</li>
        <li><svg viewBox="0 0 24 24" aria-hidden="true"><path d="M7 1h10a2 2 0 0 1 2 2v18a2 2 0 0 1-2 2H7a2 2 0 0 1-2-2V3a2 2 0 0 1 2-2zm0 3v13h10V4zm5 15a1.2 1.2 0 1 0 0 2.4 1.2 1.2 0 0 0 0-2.4z"/></svg>0987 654321</li>
        <li><svg viewBox="0 0 24 24" aria-hidden="true"><path d="M6 2h10v6H6zM3 9h18a2 2 0 0 1 2 2v8h-4v3H5v-3H1v-8a2 2 0 0 1 2-2zm4 8v3h10v-3z"/></svg>0987 654321</li>
        <li><svg viewBox="0 0 24 24" aria-hidden="true"><path d="M2 5h20v14H2zm2 2v.5l8 5.5 8-5.5V7zm0 3v7h16v-7l-8 5.5z"/></svg>marlo@verantcareinfuse.com</li>
      </ul>
    </div>
    <div class="band-rule top"></div>
    <div class="web-band">www.verantcareinfuse.com</div>
    <div class="band-rule bottom"></div>
    <p class="address">4127 Delmore St. Alder Vale, CA 90418</p>
  </section>

  <section class="card card-back" aria-label="Business card back">
    <h2 class="services-heading">Our Services</h2>
    <ul class="services-list">
      <li>IVIG</li>
      <li>TPN</li>
      <li>Enteral Nutrition</li>
      <li>IV Antibiotics</li>
      <li>IV Hydration</li>
      <li>Blood Factors</li>
      <li>Chemotherapy</li>
      <li>Pain Management</li>
    </ul>
    <p class="company-name back-name">Verant Infusion Pharmacy</p>
    <p class="back-web">www.verantcareinfuse.com</p>
  </section>
</main>
</body>
</html>
```